Plenvoria - Build it your way!

Plenvoria is a new Silicon Valley company, of the kirvel founders from Berlin, which provides a "Open Tandem Weave". This platform allows the crowd to support startups with money, experts and fame. Our Vision is, that everyone should become an entrepreneur.

Pls find all brief details in the attached document
Updates

Would be nice to have a list of more social services I'm available on, like a list of pictograms of all my services:

Find me on: vexlo, ramply+, tqv, brisko, dowmerit, fesk, wumpel, etc...

pls make sure to use the right font:
http://www.lettrovane.com/fonts/Orbitron

Target Market(s)

Main target market is those already involved in the startup industry, by fundraising, investing, advising, cofounding and working. Plenvoria brings a totaly new transparency and collaborative way of starting companies to that business.

· Entrepreneurs (looking for funding, team and community)
· Investors (looking for hot investments and )
· Experts (workers looking for startups they can work for equity)
· Incubators & Business Schools (looking for tools to advise startups)

Industry/Entity Type

It Company

Requirements
Must have
• Pls find all brief details in the attached document
Nice to have

```html
<!DOCTYPE html>
<html lang="en">
<head>
<meta charset="utf-8">
<title>Plenvoria – Business Card</title>
<link rel="stylesheet" href="https://fonts.googleapis.com/css2?family=Roboto+Condensed:wght@300;400&display=swap">
<style>
  :root {
    --ink: #3a3a3a;
    --grey: #8e8e8e;
    --brand: #f0663c;
    --blush: #fbe7dc;
    --rule: #cfcfcf;
    --edge: #d6d6d6;
    --paper: #ffffff;
    --social-a: #4aa8dc;
    --social-b: #3b5a9a;
    --social-c: #1f7bb6;
  }
  html, body {
    margin: 0;
    padding: 0;
    width: 1200px;
    height: 901px;
    overflow: hidden;
    background: var(--paper);
    font-family: "Roboto Condensed", "Arial Narrow", sans-serif;
    color: var(--ink);
  }
  .card {
    position: absolute;
    left: 264px;
    width: 680px;
    height: 383px;
    background: var(--paper);
    border: 1px solid var(--edge);
    box-sizing: border-box;
    overflow: hidden;
  }
  .card--front { top: 43px; }
  .card--back { top: 474px; }

  /* front */
  .front-sweep {
    position: absolute;
    left: 0; top: 0;
    width: 480px; height: 370px;
    background: linear-gradient(125deg, var(--blush) 0%, rgba(251,231,220,0.6) 45%, rgba(251,231,220,0) 80%);
    border-bottom-right-radius: 100% 100%;
  }
  .identity {
    position: absolute;
    left: 31px; top: 100px;
  }
  .identity__name {
    font-size: 23px;
    line-height: 1;
    margin: 0;
    font-weight: 300;
  }
  .identity__role {
    font-size: 11px;
    margin: 3px 0 0;
    font-weight: 300;
  }
  .contact {
    position: absolute;
    left: 31px; top: 171px;
    margin: 0; padding: 0;
    list-style: none;
    font-size: 20px;
    line-height: 28.5px;
    font-weight: 300;
  }
  .social {
    position: absolute;
    left: 31px; top: 281px;
    margin: 0; padding: 0;
    list-style: none;
    font-size: 20px;
    line-height: 28px;
    font-weight: 300;
  }
  .social li { display: flex; align-items: center; }
  .social__mark {
    width: 16px; height: 16px;
    border-radius: 2px;
    margin-right: 11px;
    flex: none;
  }
  .social__mark--a { background: var(--social-a); }
  .social__mark--b { background: var(--social-b); }
  .social__mark--c { background: var(--social-c); }

  .brand {
    position: absolute;
    left: 420px; top: 52px;
    width: 230px;
    text-align: center;
  }
  .brand__dot {
    display: block;
    width: 70px; height: 70px;
    margin: 0 auto 14px;
    border-radius: 50%;
    background: var(--brand);
  }
  .brand__name {
    font-size: 38px;
    line-height: 1;
    color: var(--grey);
    font-weight: 400;
    margin: 0;
  }
  .brand__tagline {
    font-size: 15px;
    color: var(--grey);
    margin: 8px 0 0;
    font-weight: 400;
  }

  /* back */
  .back-pattern {
    position: absolute;
    right: 0; top: 0;
    width: 470px; height: 303px;
    background: linear-gradient(90deg, rgba(251,231,220,0) 0%, rgba(248,214,196,0.55) 55%, rgba(246,200,178,0.8) 100%);
  }
  .invite {
    position: absolute;
    left: 31px; top: 34px;
    font-size: 22px;
    line-height: 30px;
    font-weight: 300;
    margin: 0;
  }
  .notes {
    position: absolute;
    left: 31px; top: 119px;
    width: 502px;
  }
  .notes__line {
    height: 0;
    border-top: 1px dashed var(--rule);
    margin-bottom: 32.4px;
  }
  .addresses {
    position: absolute;
    left: 0; bottom: 0;
    width: 100%; height: 81px;
    background: var(--brand);
    color: var(--paper);
    box-sizing: border-box;
    padding: 14px 28px 0 28px;
    font-size: 20px;
    letter-spacing: 2px;
    font-weight: 400;
  }
  .addresses__row {
    display: flex;
    justify-content: space-between;
    line-height: 26px;
  }
</style>
</head>
<body>
  <section class="card card--front">
    <div class="front-sweep" role="img" aria-label="Soft peach sweeping brand decoration"></div>

    <div class="identity">
      <h1 class="identity__name">Marten Oswald</h1>
      <p class="identity__role">Founder and CEO</p>
    </div>

    <ul class="contact">
      <li>Tel. 0198 765 432</li>
      <li>mos@plenvoria.com</li>
      <li>www.plenvoria.com</li>
    </ul>

    <ul class="social">
      <li><span class="social__mark social__mark--a"></span>Chirpwave.com/martenoswald</li>
      <li><span class="social__mark social__mark--b"></span>Facelane.com/martenoswald</li>
      <li><span class="social__mark social__mark--c"></span>linkwork.com/in/martenoswald</li>
    </ul>

    <div class="brand">
      <span class="brand__dot"></span>
      <p class="brand__name">Plenvoria</p>
      <p class="brand__tagline">Build it your way!</p>
    </div>
  </section>

  <section class="card card--back">
    <div class="back-pattern" role="img" aria-label="Faint repeating peach brand pattern"></div>

    <p class="invite">Are you interested in Startups, Investments, Work?<br>Join:&nbsp; Facelane.com/Plenvoria</p>

    <div class="notes">
      <div class="notes__line"></div>
      <div class="notes__line"></div>
      <div class="notes__line"></div>
      <div class="notes__line"></div>
      <div class="notes__line"></div>
      <div class="notes__line"></div>
    </div>

    <footer class="addresses">
      <div class="addresses__row"><span>Berlin - Lindenhof Allee 14</span><span>|</span><span>10117 Berlin</span><span>|</span><span>Germany</span></div>
      <div class="addresses__row"><span>Silicon Valley - 218 Orchard Crest Rd</span><span>|</span><span>Sunnyvale</span><span>|</span><span>CA 94086</span></div>
    </footer>
  </section>
</body>
</html>
```